Lumavesta.com - New Online Business
Looking For Great Business Cards and Letterhead Designs
Attention Designers:
This contest is open for 2 days for final revisions.
Teodor.
The address that can be used is
517 Pelham Ave Kingston On K7M2B9 Canada
Thanks!
Some of them are starting to look really good! There are a few things that I would like to see in all of the submissions:
-Faded line before "because it matters to you"
-Phone symbol instead of the cell phone symbol
-@ symbol instead of the envelope
-Phone number should appear as "1.888.615.4820(toll free)"
-"Lumavesta.com" should all be in capital letters the same size as eachother. Except the "O" should be biggest and the "N" should be bigger then the rest of the letters but not quite as big as the "O"
-The Lumavesta symbol needs to always be blue and grey. I like how people are doing the symbol on the back of the card but it can't be white. So the background blue color may need to fade more in the center to be able to see our symbol better.
Since it is a double sided business card I would like to see some ideas for the other side and how that can be integrated into some of these designs.
Also because there are 2 sides there is more space available. So I was considering working in the following text in some way:
"Checking the obituaries too often? Worrying that you'll miss an obituary? Here is your peace of mind!
Lumavesta.com eliminates these concerns by notifying you in the unfortunate event that a friend, colleague or loved one passes away."
I would like the subtitle "because it matters to you" to always be under the business name. Make sure it is a lowercase "b".

```html
<!DOCTYPE html>
<html lang="en">
<head>
<meta charset="utf-8">
<title>Lumavesta.com Business Cards</title>
<link rel="stylesheet" href="https://fonts.googleapis.com/css2?family=Cinzel:wght@400;600&family=Lato:wght@400&display=swap">
<style>
  :root {
    --backdrop: #d9dcdf;
    --navy: #1a4279;
    --steel: #8594a5;
    --steel-dark: #6f7f92;
    --paper: #ffffff;
    --tagline: #7a8594;
    --line-fade: #9aa5b2;
  }
  * { box-sizing: border-box; margin: 0; padding: 0; }
  html, body { width: 1200px; height: 826px; overflow: hidden; }
  body { background: var(--backdrop); position: relative; font-family: "Cinzel", serif; }

  .card { position: absolute; border-radius: 12px; overflow: hidden; }

  .card-front { left: 331px; top: 139px; width: 490px; height: 288px; background: linear-gradient(180deg, var(--steel) 0%, var(--steel-dark) 100%); }
  .card-front .bands { position: absolute; inset: 0; width: 100%; height: 100%; }

  .holder { position: absolute; right: 24px; top: 18px; text-align: right; color: var(--paper); }
  .holder-name { font-size: 19px; font-weight: 600; letter-spacing: 1px; line-height: 1.2; }
  .holder-role { font-size: 10px; letter-spacing: 1.5px; margin-top: 2px; }

  .brand { position: absolute; left: 100px; top: 112px; display: flex; align-items: center; gap: 10px; }
  .brand-mark { width: 30px; height: 30px; background: var(--navy); flex: none; }
  .brand-name { font-size: 26px; font-weight: 600; color: var(--navy); letter-spacing: .5px; line-height: 1; }
  .tagline { position: absolute; right: 88px; top: 154px; display: flex; align-items: center; gap: 6px; font-family: "Lato", sans-serif; font-size: 11px; color: var(--tagline); }
  .tagline-rule { width: 60px; height: 1px; background: linear-gradient(90deg, rgba(154,165,178,0), var(--line-fade)); }

  .contact { position: absolute; left: 20px; top: 232px; color: var(--paper); font-size: 10px; line-height: 1.7; letter-spacing: .5px; }

  .card-back-light { left: 89px; top: 451px; width: 482px; height: 274px; background: var(--paper); }
  .card-back-dark { left: 592px; top: 451px; width: 486px; height: 274px; background: radial-gradient(circle at 50% 45%, #2a5a98 0%, var(--navy) 70%); }

  .back-brand { position: absolute; inset: 0; display: flex; flex-direction: column; align-items: center; justify-content: center; gap: 14px; }
  .back-circle { width: 64px; height: 64px; border-radius: 50%; }
  .back-name { font-size: 26px; font-weight: 600; letter-spacing: 1px; line-height: 1; }
  .card-back-light .back-circle { background: var(--navy); }
  .card-back-light .back-name { color: var(--navy); }
  .card-back-dark .back-circle { background: var(--steel); }
  .card-back-dark .back-name { color: var(--paper); }
</style>
</head>
<body>

<section class="card card-front">
  <svg class="bands" viewBox="0 0 490 288" preserveAspectRatio="none" aria-hidden="true">
    <polygon points="0,60 135,12 165,12 490,70 490,84 165,26 135,26 0,74" fill="var(--navy)"/>
    <polygon points="0,74 135,26 165,26 490,84 490,205 365,250 285,200 0,200" fill="var(--paper)"/>
    <polygon points="0,200 285,200 365,250 490,205 490,219 365,264 285,214 0,214" fill="var(--navy)"/>
  </svg>

  <div class="holder">
    <div class="holder-name">Bren Moorcroft</div>
    <div class="holder-role">Owner</div>
  </div>

  <div class="brand">
    <span class="brand-mark"></span>
    <span class="brand-name">LUMAVESTA.COM</span>
  </div>
  <div class="tagline">
    <span class="tagline-rule"></span>
    <span>because it matters to you</span>
  </div>

  <div class="contact">
    <div>T : 1.888.615.4820</div>
    <div>E : BREN@LUMAVESTA.COM</div>
  </div>
</section>

<section class="card card-back-light">
  <div class="back-brand">
    <span class="back-circle"></span>
    <span class="back-name">LUMAVESTA.COM</span>
  </div>
</section>

<section class="card card-back-dark">
  <div class="back-brand">
    <span class="back-circle"></span>
    <span class="back-name">LUMAVESTA.COM</span>
  </div>
</section>

</body>
</html>
```